Surgical Procedure Room Letterhead

PLEASE DO NOT MAKE YOUR LETTERHEAD SIMILAR TO THE ONE I AM INCLUDING IN MY UPLOADS

Hello! I need my logo used to make a very clean, professional, simple letterhead that has all the pertinent information in it:
Location: 4182 NW 38th Lane, Suite 500
Cedar Point, GA 33967
Phone: 954-218-4650
Fax: 800-642-9082

Can you please put this all on a word document that is easily editable? I will include my practice letterhead as an example ONLY of how easy it should be to write below the letterhead. Please don't make this letterhead the same as the one I am including in this example. They are two separate businesses.

Target Market(s)

Insurance companies

Industry/Entity Type

medical

Requirements
Must have
• classiness, elegance, simplicity
Should not have
• Please don't make your letterhead the same as the one that I included in my uploads

```html
<!DOCTYPE html>
<html lang="en">
<head>
<meta charset="UTF-8">
<title>Meridian Care Suites Letterhead</title>
<link href="https://fonts.googleapis.com/css2?family=Poppins:wght@400;600&display=swap" rel="stylesheet">
<style>
  :root {
    --backdrop: #616161;
    --paper: #ffffff;
    --navy: #1b3260;
    --gold: #d9b642;
    --ink: #1b3260;
  }
  * { margin: 0; padding: 0; box-sizing: border-box; }
  html, body {
    width: 1200px;
    height: 686px;
    overflow: hidden;
    background: var(--backdrop);
  }
  .canvas {
    position: relative;
    width: 1200px;
    height: 686px;
  }
  .letterhead {
    position: absolute;
    left: 374px;
    top: 23px;
    width: 452px;
    height: 640px;
    background: var(--paper);
    font-family: "Poppins", sans-serif;
    color: var(--ink);
  }
  .letterhead__header {
    position: absolute;
    top: 40px;
    left: 36px;
    right: 36px;
    display: flex;
    align-items: center;
  }
  .brand {
    display: flex;
    align-items: center;
    gap: 8px;
  }
  .brand__dot {
    width: 24px;
    height: 24px;
    border-radius: 50%;
    background: var(--gold);
    flex: none;
  }
  .brand__name {
    font-family: "Poppins", sans-serif;
    font-weight: 600;
    font-size: 13px;
    line-height: 1.15;
    letter-spacing: 0.06em;
    text-transform: uppercase;
    color: var(--navy);
  }
  .header__divider {
    width: 1.5px;
    height: 54px;
    background: var(--gold);
    margin: 0 14px 0 26px;
    flex: none;
  }
  .contact {
    list-style: none;
    font-size: 8.5px;
    line-height: 1.45;
    color: var(--ink);
  }
  .contact__item {
    display: flex;
    align-items: flex-start;
    gap: 6px;
  }
  .contact__icon {
    width: 8px;
    height: 8px;
    margin-top: 3px;
    flex: none;
  }
  .letterhead__footer {
    position: absolute;
    left: 0;
    bottom: 0;
    width: 452px;
    height: 40px;
  }
</style>
</head>
<body>
<div class="canvas">
  <article class="letterhead">
    <header class="letterhead__header">
      <div class="brand">
        <span class="brand__dot"></span>
        <span class="brand__name">Meridian<br>Care Suites</span>
      </div>
      <span class="header__divider"></span>
      <ul class="contact">
        <li class="contact__item">
          <svg class="contact__icon" viewBox="0 0 10 10"><path d="M2 1 L4 1 L4.8 3.2 L3.6 4 Q4.6 6 6 6.4 L6.8 5.2 L9 6 L9 8 Q8 9.2 6 8.6 Q2.2 7 1.2 3 Q1 1.6 2 1 Z" fill="var(--gold)"/></svg>
          <span>954-218-4650</span>
        </li>
        <li class="contact__item">
          <svg class="contact__icon" viewBox="0 0 10 10"><rect x="1" y="4" width="8" height="5" rx="1" fill="var(--gold)"/><rect x="3" y="1" width="4" height="3" fill="var(--gold)"/></svg>
          <span>800-642-9082</span>
        </li>
        <li class="contact__item">
          <svg class="contact__icon" viewBox="0 0 10 10"><path d="M5 0.6 A3.2 3.2 0 0 1 8.2 3.8 Q8.2 6 5 9.4 Q1.8 6 1.8 3.8 A3.2 3.2 0 0 1 5 0.6 Z" fill="var(--gold)"/><circle cx="5" cy="3.8" r="1.2" fill="#fff"/></svg>
          <span>4182 NW 38th Lane,<br>Suite 500, Cedar Point, GA 33967</span>
        </li>
      </ul>
    </header>

    <svg class="letterhead__footer" viewBox="0 0 452 40" aria-hidden="true">
      <path d="M0 40 L0 33 L335 33 Q341 33 343 28 Q345 24 351 24 L452 24 L452 40 Z" fill="var(--gold)"/>
      <path d="M0 26 L331 26 Q335 26 336 23 L337 21 L0 21 Z" fill="var(--navy)"/>
    </svg>
  </article>
</div>
</body>
</html>
```